OTT TV and VOD Service Website (like Kestrova.tv ; Vexo etc.)

Site will be used as a marketing page integrated with subscription processing (Quandle). Looking for someone with solid experience in designing video content driven sites. For the looks; clean, modern, black background with rich "popping" VOD and live TV channel titles.

Video-on-demand and international live TV channel subscribers in Asia

Coded - Design and coding required

5+ page

• See files

Requirements
Must have
• Start with an awesome looking "coming soon" page, featuring a logo on black background with video (i.e. a movie trailers) playing in the background. This page should also have an understated "about" link and an email "contact" form.
Site: Scrollable interfaces: Service / Live Channels / VOD / Subscribe.
Contrasting backgrounds as the page is being scrolled. Black as a dominating background color. See Kestrova.tv site for inspiration
There will be contact form (Register)
Nice to have
• Dynamic video background on the home page (trailer / title / channel promo)
Clear interface separation between live TV channels and VOD
Should not have
• Typical template looking scrolling site with boring icons and

```html
<!DOCTYPE html>
<html lang="en">
<head>
<meta charset="utf-8">
<title>Lumora.tv – International Live TV Channel</title>
<link rel="stylesheet" href="https://fonts.googleapis.com/css2?family=Source+Sans+3:wght@300;400;600;700&display=swap">
<style>
:root{
  --ink:#222;
  --muted:#777;
  --dark:#1f1f23;
  --dark-2:#2b2b31;
  --card:#2a2a2e;
  --white:#fff;
  --blue:#27a9e1;
  --green:#8dc63f;
  --accent:linear-gradient(90deg,var(--blue),var(--green));
  --rule:#d8d8d8;
}
*{margin:0;padding:0;box-sizing:border-box}
html,body{width:1200px;height:3653px;overflow:hidden}
body{position:relative;font-family:"Source Sans 3",sans-serif;color:var(--ink);background:var(--white)}
.abs{position:absolute}
.btn{position:absolute;display:flex;align-items:center;justify-content:center;font-size:12px;font-weight:700;letter-spacing:.3px;text-transform:uppercase;color:var(--white);background:var(--accent)}
.photo{position:absolute;overflow:hidden}
.section-title{position:absolute;left:0;width:1200px;text-align:center;font-weight:300;font-size:33px;color:#333}

/* hero */
.hero{position:absolute;left:0;top:0;width:1200px;height:390px;background:linear-gradient(100deg,#1d6f86 0%,#2b7f8a 45%,#4d8d5a 80%,#6a9a3c 100%)}
.logo{position:absolute;font-weight:700;color:var(--white)}
.nav a{position:absolute;top:31px;font-size:11px;font-weight:600;color:var(--white);text-decoration:none;letter-spacing:.2px}
.nav-rule{position:absolute;left:94px;top:73px;width:1012px;height:1px;background:rgba(255,255,255,.3)}
.login{position:absolute;left:1018px;top:22px;width:88px;height:31px;border:1px solid var(--white);color:var(--white);font-size:11px;font-weight:700;display:flex;align-items:center;justify-content:center}
.hero h1{position:absolute;left:0;top:168px;width:1200px;text-align:center;font-weight:300;font-size:48px;color:var(--white)}
.hero .cta{position:absolute;left:516px;top:240px;width:168px;height:44px;background:var(--white);color:#111;font-size:12px;font-weight:700;display:flex;align-items:center;justify-content:center}

/* vod band */
.vod-band{position:absolute;left:0;top:390px;width:1200px;height:149px;background:var(--dark)}
.vod-band h2{position:absolute;left:300px;top:45px;font-weight:300;font-size:40px;color:var(--white)}

/* mosaic */
.tile-cap{position:absolute;left:20px;bottom:20px;color:var(--white)}
.tile-cap small{display:block;font-size:11px;font-weight:600;text-transform:uppercase}
.tile-cap strong{display:block;font-size:25px;font-weight:300;line-height:1.2}
.tile-cap em{display:block;font-style:normal;font-size:11px}

/* carousels */
.arrow{position:absolute;width:30px;height:48px;background:rgba(0,0,0,.45);display:flex;align-items:center;justify-content:center}
.live-badge{position:absolute;left:8px;top:10px;padding:1px 8px;border-radius:8px;font-size:10px;font-weight:700;color:var(--white);background:var(--accent)}
.play-cap{position:absolute;left:12px;bottom:14px;display:flex;align-items:center;gap:10px;color:var(--white);font-size:14px}
.play-cap svg{flex:none}

/* tv shows */
.shows{position:absolute;left:0;top:1289px;width:1200px;height:345px;background:radial-gradient(ellipse at 75% 40%,#4a4a52 0%,#2b2b31 55%,#232328 100%)}
.shows h2{position:absolute;left:90px;top:104px;font-weight:300;font-size:40px;color:var(--white)}
.shows p{position:absolute;left:94px;top:153px;width:360px;font-size:15px;line-height:1.6;color:#ddd}

/* movies */
.movie-name{position:absolute;font-size:15px;font-weight:600;color:#222}
.movie-genre{position:absolute;font-size:11px;color:var(--muted)}
.rating{position:absolute;width:24px;height:24px;border-radius:50%;border:2px solid var(--green);color:var(--white);font-size:10px;display:flex;align-items:center;justify-content:center}
.divider{position:absolute;left:94px;top:2092px;width:1012px;height:1px;background:var(--rule)}
.vod-cap{position:absolute;left:12px;bottom:14px;display:flex;gap:12px;align-items:center;color:var(--white)}
.vod-cap strong{display:block;font-size:15px;font-weight:600}
.vod-cap em{display:block;font-style:normal;font-size:11px}

/* plans */
.plans{position:absolute;left:0;top:2387px;width:1200px;height:663px;background:var(--dark-2)}
.plans .section-title{color:var(--white);top:42px;font-size:40px}
.plan{position:absolute;background:var(--card);border-top:4px solid;border-image:var(--accent) 1;box-shadow:0 20px 30px rgba(0,0,0,.35);color:var(--white);text-align:center}
.plan h3{margin-top:24px;font-size:12px;font-weight:700;text-transform:uppercase}
.plan .lead{margin-top:10px;font-size:17px;font-weight:300}
.plan .price{margin-top:6px;font-size:34px;font-weight:400}
.plan .price span{font-size:14px}
.plan ul{list-style:none;text-align:left;margin:14px 18px 0 18px}
.plan li{position:relative;padding-left:26px;font-size:12px;line-height:1.35;color:#ddd;margin-bottom:17px}
.plan li svg{position:absolute;left:0;top:2px}
.plan .btn{position:relative;margin:10px auto 0;width:122px;height:40px}

/* app promo */
.promo h2{position:absolute;left:176px;top:3110px;font-weight:300;font-size:35px;color:#222}
.promo h2 b{font-weight:600}

/* footer */
.footer{position:absolute;left:0;top:3279px;width:1200px;height:374px;background:var(--dark)}
.footer .col{position:absolute;top:101px;list-style:none}
.footer .col li{font-size:12px;color:#9a9aa0;line-height:28px}
.social{position:absolute;top:236px;width:18px;height:18px;border-radius:50%;background:#d6d6d6}
.footer-rule{position:absolute;left:94px;top:311px;width:1012px;height:1px;background:#3a3a40}
.store{position:absolute;top:329px;height:34px;border-radius:4px;border:1px solid #666;background:#000}
.copy{position:absolute;left:0;top:339px;width:1200px;text-align:center;font-size:11px;color:#8a8a90}
.copy b{color:var(--blue);font-weight:400}
.to-top{position:absolute;left:1055px;top:326px;width:39px;height:39px;border:1px solid #bbb;display:flex;align-items:center;justify-content:center}
</style>
</head>
<body>

<!-- hero -->
<header class="hero" role="img" aria-label="Wall of television screens showing channel imagery, tinted blue to green">
  <div class="logo" style="left:94px;top:17px;font-size:34px">Lumora.tv</div>
  <nav class="nav">
    <a style="left:275px">HOME</a>
    <a style="left:353px">SERVICE</a>
    <a style="left:445px">LIVE CHANNELS</a>
    <a style="left:577px">PRICING PLAN</a>
    <a style="left:700px">ABOUT US</a>
  </nav>
  <div class="login">LOGIN</div>
  <div class="nav-rule"></div>
  <h1>International Live TV Channel</h1>
  <div class="cta">SUBSCRIBE NOW</div>
</header>

<section class="vod-band">
  <h2>Video On Demand (VOD)</h2>
  <div class="btn" style="left:740px;top:54px;width:160px;height:42px">Subscribe Now</div>
</section>

<!-- featured VOD mosaic -->
<section class="mosaic">
  <div class="photo" style="left:94px;top:539px;width:338px;height:454px;background:linear-gradient(180deg,#b9c7d3 0%,#c9a7a8 55%,#8a6f6a 100%)" role="img" aria-label="Woman in a pink dress and straw hat by a seaside window">
    <div class="tile-cap"><small>Vel commodo</small><strong>Pellentesque</strong><em>Action, Triler</em></div>
  </div>
  <div class="photo" style="left:432px;top:539px;width:338px;height:227px;background:linear-gradient(135deg,#3a1c3a,#9a3d6a 60%,#d36a7e)" role="img" aria-label="Musician playing an acoustic guitar on stage">
    <div class="tile-cap"><small>Curabitur</small><strong>Sollicitudin</strong><em>Romance, Drama</em></div>
  </div>
  <div class="photo" style="left:432px;top:766px;width:338px;height:227px;background:linear-gradient(135deg,#1a1030,#4b2a8a 55%,#8c3cc4)" role="img" aria-label="Film poster artwork in purple stage light">
    <div class="tile-cap"><small>Donec</small><strong>Imperdiet</strong><em>Comedy</em></div>
  </div>
  <div class="photo" style="left:770px;top:539px;width:336px;height:151px;background:linear-gradient(135deg,#1a0d0d,#6a1a1a 60%,#c24a3a)" role="img" aria-label="Singer recording in a studio with a microphone">
    <div class="tile-cap"><small>Pellentesque</small><strong>Fringilla</strong><em>Comedy</em></div>
  </div>
  <div class="photo" style="left:770px;top:690px;width:336px;height:152px;background:linear-gradient(135deg,#111,#3a3a3e 60%,#8a8a8e)" role="img" aria-label="Dancer leaping through stage smoke">
    <div class="tile-cap"><small>Proin</small><strong>Ornare</strong><em>Drama</em></div>
  </div>
  <div class="photo" style="left:770px;top:842px;width:336px;height:151px;background:linear-gradient(135deg,#0b3a6a,#1c6fb0 60%,#5aa8d8)" role="img" aria-label="Swimmer splashing in a pool">
    <div class="tile-cap"><small>Morbi</small><strong>Faucibus</strong><em>Comedy</em></div>
  </div>
</section>

<!-- live channels -->
<h2 class="section-title" style="top:1038px">Live Channels</h2>
<section class="live">
  <div class="photo" style="left:94px;top:1100px;width:191px;height:130px;background:linear-gradient(160deg,#111,#3a2a20 70%,#6a4a30)" role="img" aria-label="Dancers on a dark stage">
    <span class="live-badge">LIVE</span><div class="play-cap"><svg width="10" height="12"><path d="M0 0L10 6L0 12Z" fill="#fff"/></svg>Etiam rutrum</div></div>
  <div class="photo" style="left:299px;top:1100px;width:191px;height:130px;background:linear-gradient(160deg,#4a3a2a,#3a6a3a 60%,#2a4a2a)" role="img" aria-label="Tennis stadium from above">
    <span class="live-badge">LIVE</span><div class="play-cap"><svg width="10" height="12"><path d="M0 0L10 6L0 12Z" fill="#fff"/></svg>Etiam rutrum</div></div>
  <div class="photo" style="left:504px;top:1100px;width:191px;height:130px;background:linear-gradient(160deg,#1a1040,#5a2a8a 60%,#d0602a)" role="img" aria-label="Performer under colourful concert lights">
    <span class="live-badge">LIVE</span><div class="play-cap"><svg width="10" height="12"><path d="M0 0L10 6L0 12Z" fill="#fff"/></svg>Etiam rutrum</div></div>
  <div class="photo" style="left:709px;top:1100px;width:191px;height:130px;background:linear-gradient(160deg,#8aa0b0,#a09080 60%,#6a6a6a)" role="img" aria-label="Skateboarder in a skate park">
    <span class="live-badge">LIVE</span><div class="play-cap"><svg width="10" height="12"><path d="M0 0L10 6L0 12Z" fill="#fff"/></svg>Etiam rutrum</div></div>
  <div class="photo" style="left:915px;top:1100px;width:191px;height:130px;background:linear-gradient(160deg,#4a4a4a,#2a2a2a 60%,#1a1a1a)" role="img" aria-label="Singer performing at a microphone">
    <span class="live-badge">LIVE</span><div class="play-cap"><svg width="10" height="12"><path d="M0 0L10 6L0 12Z" fill="#fff"/></svg>Etiam rutrum</div></div>
  <div class="arrow" style="left:76px;top:1141px"><svg width="10" height="18"><path d="M9 1L1 9L9 17" stroke="#fff" stroke-width="1.6" fill="none"/></svg></div>
  <div class="arrow" style="left:1092px;top:1141px"><svg width="10" height="18"><path d="M1 1L9 9L1 17" stroke="#fff" stroke-width="1.6" fill="none"/></svg></div>
</section>

<!-- tv shows -->
<section class="shows">
  <h2>Enjoy Your TV Shows</h2>
  <p>Aenean tempus pellentesque pellentesque. Vivamus eu nisl quam phasellus sed tempor nunc</p>
  <div class="btn" style="left:94px;top:225px;width:137px;height:43px">Try It Now</div>
  <div class="photo" style="left:596px;top:46px;width:374px;height:208px;border:3px solid #555;background:linear-gradient(135deg,#0e1a2a,#1d3a5a 50%,#2a5a7a)" role="img" aria-label="Television showing a grid of show thumbnails"></div>
  <div class="abs" style="left:692px;top:254px;width:180px;height:8px;background:#111"></div>
  <div class="abs" style="left:518px;top:262px;width:528px;height:22px;background:linear-gradient(180deg,#222,#111);box-shadow:0 14px 20px rgba(0,0,0,.4)"></div>
</section>

<!-- popular movies -->
<h2 class="section-title" style="top:1684px">Popular Movies</h2>
<section class="movies">
  <div class="photo" style="left:94px;top:1747px;width:184px;height:246px;background:linear-gradient(180deg,#2a3a3a,#4a5a5a 60%,#6a5a40)" role="img" aria-label="Figure in a misty forest with headlights"><span class="rating" style="left:148px;top:14px">8.5</span></div>
  <div class="photo" style="left:301px;top:1747px;width:184px;height:246px;background:linear-gradient(160deg,#2a1060,#8a2aa0 55%,#3a40c0)" role="img" aria-label="Portrait in neon pink and blue light"><span class="rating" style="left:148px;top:14px">7.5</span></div>
  <div class="photo" style="left:508px;top:1747px;width:184px;height:246px;background:linear-gradient(180deg,#c8c0b0,#9a8a70 60%,#6a5a40)" role="img" aria-label="Two wasteland warriors in a desert"><span class="rating" style="left:148px;top:14px">7.0</span></div>
  <div class="photo" style="left:715px;top:1747px;width:184px;height:246px;background:linear-gradient(180deg,#2a2a28,#4a4a40 60%,#1a1a18)" role="img" aria-label="Masked figure in shadow"><span class="rating" style="left:148px;top:14px">8.0</span></div>
  <div class="photo" style="left:922px;top:1747px;width:184px;height:246px;background:linear-gradient(180deg,#e0e4e8,#b07a50 55%,#6a4a30)" role="img" aria-label="Metallic robot skeleton"><span class="rating" style="left:148px;top:14px">8.2</span></div>
  <div class="movie-name" style="left:94px;top:1997px">Lorem ipsum</div><div class="movie-genre" style="left:94px;top:2018px">Romance, Drama</div>
  <div class="movie-name" style="left:301px;top:1997px">Lorem ipsum</div><div class="movie-genre" style="left:301px;top:2018px">Romance, Drama</div>
  <div class="movie-name" style="left:508px;top:1997px">Lorem ipsum</div><div class="movie-genre" style="left:508px;top:2018px">Romance, Drama</div>
  <div class="movie-name" style="left:715px;top:1997px">Lorem ipsum</div><div class="movie-genre" style="left:715px;top:2018px">Romance, Drama</div>
  <div class="movie-name" style="left:922px;top:1997px">Lorem ipsum</div><div class="movie-genre" style="left:922px;top:2018px">Romance, Drama</div>
  <div class="arrow" style="left:76px;top:1854px"><svg width="10" height="18"><path d="M9 1L1 9L9 17" stroke="#fff" stroke-width="1.6" fill="none"/></svg></div>
  <div class="arrow" style="left:1092px;top:1854px"><svg width="10" height="18"><path d="M1 1L9 9L1 17" stroke="#fff" stroke-width="1.6" fill="none"/></svg></div>
</section>
<div class="divider"></div>

<!-- video on demand -->
<h2 class="section-title" style="top:2113px">Video On Demand</h2>
<section class="vod">
  <div class="photo" style="left:94px;top:2172px;width:238px;height:160px;background:linear-gradient(160deg,#0a0a10,#3a2a30 60%,#6a4a50)" role="img" aria-label="Fireworks over a dark sky">
    <div class="vod-cap"><svg width="10" height="12"><path d="M0 0L10 6L0 12Z" fill="#fff"/></svg><div><strong>Quisque malesuada</strong><em>Romance, Drama</em></div></div></div>
  <div class="photo" style="left:352px;top:2172px;width:238px;height:160px;background:linear-gradient(160deg,#3a6a4a,#6a8a3a 50%,#2a5a6a)" role="img" aria-label="Peacock with fanned tail feathers">
    <div class="vod-cap"><svg width="10" height="12"><path d="M0 0L10 6L0 12Z" fill="#fff"/></svg><div><strong>Quisque malesuada</strong><em>Romance, Drama</em></div></div></div>
  <div class="photo" style="left:610px;top:2172px;width:238px;height:160px;background:linear-gradient(160deg,#2a2a2a,#8a7040 55%,#3a3a3a)" role="img" aria-label="Singer in a gold outfit on stage">
    <div class="vod-cap"><svg width="10" height="12"><path d="M0 0L10 6L0 12Z" fill="#fff"/></svg><div><strong>Quisque malesuada</strong><em>Romance, Drama</em></div></div></div>
  <div class="photo" style="left:868px;top:2172px;width:238px;height:160px;background:linear-gradient(180deg,#c0c8c0,#6a8a5a 60%,#4a7a4a)" role="img" aria-label="Tennis player serving on grass court">
    <div class="vod-cap"><svg width="10" height="12"><path d="M0 0L10 6L0 12Z" fill="#fff"/></svg><div><strong>Quisque malesuada</strong><em>Romance, Drama</em></div></div></div>
  <div class="arrow" style="left:76px;top:2228px"><svg width="10" height="18"><path d="M9 1L1 9L9 17" stroke="#fff" stroke-width="1.6" fill="none"/></svg></div>
  <div class="arrow" style="left:1092px;top:2228px"><svg width="10" height="18"><path d="M1 1L9 9L1 17" stroke="#fff" stroke-width="1.6" fill="none"/></svg></div>
</section>

<!-- plans -->
<section class="plans">
  <h2 class="section-title">Select Your Plan</h2>

  <article class="plan" style="left:166px;top:135px;width:281px;height:425px">
    <h3>Quisque malesuada</h3>
    <p class="lead">Get 1 month free, then starts at</p>
    <p class="price">$4.50/ <span>month</span></p>
    <ul>
      <li><svg width="14" height="11"><path d="M1 6L5 10L13 1" stroke="#8dc63f" stroke-width="2" fill="none"/></svg>Nunc feugiat nulla non scel pellentesque. Etiam tristique vestibulum interdum.</li>
      <li><svg width="14" height="11"><path d="M1 6L5 10L13 1" stroke="#8dc63f" stroke-width="2" fill="none"/></svg>Orci varius natoque penatibus et magnis dis parturient montes,</li>
      <li><svg width="14" height="11"><path d="M1 6L5 10L13 1" stroke="#8dc63f" stroke-width="2" fill="none"/></svg>Aliquam egestas scelerisque vestibulum. Quisque tincidunt eget eros.</li>
      <li><svg width="14" height="11"><path d="M1 6L5 10L13 1" stroke="#8dc63f" stroke-width="2" fill="none"/></svg>Praesent ultrices por tellus a sollicitudin. Pellentesque finibus orci eu nulla luctus tempus</li>
    </ul>
    <div class="btn">Buy Now</div>
  </article>

  <article class="plan" style="left:460px;top:112px;width:280px;height:470px;padding-top:23px">
    <h3>Quisque malesuada</h3>
    <p class="lead">Get 1 month free, then starts at</p>
    <p class="price">$4.50/ <span>month</span></p>
    <ul>
      <li><svg width="14" height="11"><path d="M1 6L5 10L13 1" stroke="#8dc63f" stroke-width="2" fill="none"/></svg>Nunc feugiat nulla non scel pellentesque. Etiam tristique vestibulum interdum.</li>
      <li><svg width="14" height="11"><path d="M1 6L5 10L13 1" stroke="#8dc63f" stroke-width="2" fill="none"/></svg>Orci varius natoque penatibus et magnis dis parturient montes,</li>
      <li><svg width="14" height="11"><path d="M1 6L5 10L13 1" stroke="#8dc63f" stroke-width="2" fill="none"/></svg>Aliquam egestas scelerisque vestibulum. Quisque tincidunt eget eros.</li>
      <li><svg width="14" height="11"><path d="M1 6L5 10L13 1" stroke="#8dc63f" stroke-width="2" fill="none"/></svg>Praesent ultrices por tellus a sollicitudin. Pellentesque finibus orci eu nulla luctus tempus</li>
    </ul>
    <div class="btn">Buy Now</div>
  </article>

  <article class="plan" style="left:753px;top:135px;width:281px;height:425px">
    <h3>Quisque malesuada</h3>
    <p class="lead">Get 1 month free, then starts at</p>
    <p class="price">$4.50/ <span>month</span></p>
    <ul>
      <li><svg width="14" height="11"><path d="M1 6L5 10L13 1" stroke="#8dc63f" stroke-width="2" fill="none"/></svg>Nunc feugiat nulla non scel pellentesque. Etiam tristique vestibulum interdum.</li>
      <li><svg width="14" height="11"><path d="M1 6L5 10L13 1" stroke="#8dc63f" stroke-width="2" fill="none"/></svg>Orci varius natoque penatibus et magnis dis parturient montes,</li>
      <li><svg width="14" height="11"><path d="M1 6L5 10L13 1" stroke="#8dc63f" stroke-width="2" fill="none"/></svg>Aliquam egestas scelerisque vestibulum. Quisque tincidunt eget eros.</li>
      <li><svg width="14" height="11"><path d="M1 6L5 10L13 1" stroke="#8dc63f" stroke-width="2" fill="none"/></svg>Praesent ultrices por tellus a sollicitudin. Pellentesque finibus orci eu nulla luctus tempus</li>
    </ul>
    <div class="btn">Buy Now</div>
  </article>
</section>

<!-- app promo -->
<section class="promo">
  <h2>Watch Thousands of <b>Shows</b> and <b>Movies</b></h2>
  <div class="btn" style="left:176px;top:3168px;width:160px;height:45px">Subscribe Now</div>
  <div class="photo" style="left:802px;top:3156px;width:178px;height:110px;border:4px solid #111;border-radius:10px;background:linear-gradient(135deg,#2a1a4a,#8a2a8a 55%,#d04a8a)" role="img" aria-label="Tablet showing a dancing performer"></div>
  <div class="photo" style="left:950px;top:3055px;width:110px;height:220px;border:4px solid #111;border-radius:14px;background:linear-gradient(180deg,#0a0a12,#2a1a3a 55%,#8a3a2a)" role="img" aria-label="Phone showing a saxophone player"></div>
</section>

<!-- footer -->
<footer class="footer">
  <div class="logo" style="left:94px;top:76px;font-size:62px;color:var(--blue)">Lumora.tv</div>
  <ul class="col" style="left:417px"><li>Streaming Library</li><li>Live TV</li><li>Live News</li><li>Live Sports</li></ul>
  <ul class="col" style="left:640px"><li>TV Shows</li><li>Movies</li><li>Originals</li><li>Networks</li><li>Kids</li></ul>
  <ul class="col" style="left:815px"><li>Help Centre</li><li>Jobs</li><li>Cookie Preferences</li><li>Legal Notices</li></ul>
  <ul class="col" style="left:1030px"><li>Home</li><li>Service</li><li>Live Channels</li><li>Pricing Plan</li><li>About Us</li></ul>
  <span class="social" style="left:90px"></span>
  <span class="social" style="left:129px"></span>
  <span class="social" style="left:169px"></span>
  <span class="social" style="left:209px"></span>
  <div class="footer-rule"></div>
  <span class="store" style="left:94px;width:100px"></span>
  <span class="store" style="left:210px;width:120px"></span>
  <p class="copy">© 2020 <b>Lumora.tv</b>. All Right Reserved.</p>
  <div class="to-top"><svg width="12" height="20"><path d="M6 19V2M1 7L6 2L11 7" stroke="#ddd" stroke-width="1.5" fill="none"/></svg></div>
</footer>

</body>
</html>
```